Wood Bamboo Print Website

We like a brand new design for our wood bamboo print website. We print photo's and mount them on bamboo panels. klemvit dot com

We'd like a clean vintage/urban design

Design must at least contain:

Logo
Menu
Banner
The 2 options we have 2.5cm bamboo and 4cm bamboo hanging and standing
Upload photo button
Some text for UPS
LEt your imagination do the rest :)

Homepage
CMS page

Show responsive design

Design must be according bootstrap 3.0 rules

```html
<!DOCTYPE html>
<html lang="en">
<head>
<meta charset="utf-8">
<title>Klemvit Bamboo Prints</title>
<link href="https://fonts.googleapis.com/css2?family=Cabin:ital,wght@0,400;0,700;1,700&display=swap" rel="stylesheet">
<style>
:root{
  --page:#efe5cc;
  --white:#ffffff;
  --text:#7a7a7a;
  --nav-text:#111111;
  --green:#5a9e22;
  --green-dark:#4a861a;
  --footer:#4b4b4d;
  --panel:#f0f0f0;
  --panel-border:#c9c9c9;
  --wood-light:#d8c8a2;
  --wood-mid:#b9a67e;
  --slate:#6f6f72;
}
*{box-sizing:border-box;margin:0;padding:0}
html,body{width:1159px;height:1200px;overflow:hidden}
body{background:var(--page);font-family:'Cabin',sans-serif;position:relative}
.site-logo{position:absolute;left:174px;top:18px;width:173px;height:86px;background:var(--white);display:flex;align-items:center;justify-content:center;gap:8px}
.site-logo .mark{width:14px;height:14px;background:var(--green)}
.site-logo .name{font-size:26px;font-weight:700;color:var(--green);letter-spacing:.5px}
.main-nav{position:absolute;left:174px;top:118px;width:816px;height:32px}
.main-nav svg{position:absolute;left:0;top:0}
.main-nav ul{list-style:none;position:relative}
.main-nav li{position:absolute;top:0;height:32px;line-height:32px;font-size:11.5px;font-weight:700;font-style:italic;color:var(--nav-text);transform:translateX(-50%);white-space:nowrap}
.main-nav li.active{top:-5px;height:28px;line-height:26px;width:143px;text-align:center;background:var(--green);border-bottom:3px solid var(--green-dark)}
.hero-banner{position:absolute;left:174px;top:151px;width:812px;height:257px;background:linear-gradient(160deg,#5d5d60 0%,#8a8275 35%,var(--wood-mid) 60%,#7c766c 100%)}
.content-panel{position:absolute;left:174px;top:417px;width:812px;height:783px;background:var(--white)}
.body-copy{position:absolute;left:41px;width:731px;font-size:10.4px;line-height:17.3px;color:var(--text);text-align:justify;letter-spacing:.15px}
.intro{top:26px}
.more{top:341px}
.promo-video{position:absolute;left:41px;top:175px;width:268px;height:150px;background:linear-gradient(135deg,#3b3430,#8a7a6a 55%,#2d2d2d)}
.upload-box{position:absolute;left:483px;top:183px;width:282px;height:118px;background:var(--panel);border:2px solid var(--panel-border);border-radius:18px;box-shadow:0 0 3px rgba(0,0,0,.25);padding:14px 12px;font-size:10.5px;color:#888}
.upload-box .row{display:flex;align-items:center;gap:5px}
.upload-box .btn{font-family:'Cabin',sans-serif;font-size:10.5px;color:#111;background:linear-gradient(#f7f7f7,#dcdcdc);border:1px solid #8a8a8a;border-radius:2px;padding:1px 8px}
.upload-box .submit{margin-top:16px;padding:1px 4px}
.gallery{position:absolute;left:20px;top:480px;display:flex;gap:23px}
.gallery .photo{width:243px;height:188px}
.p1{background:linear-gradient(135deg,#3a2f28,#e8e0c8 45%,#d6c294)}
.p2{background:linear-gradient(135deg,#6a6a6c,var(--wood-light) 50%,#77767a)}
.p3{background:linear-gradient(135deg,#2a2620,#c9b98e 50%,#d6c8a4)}
.gallery-caption{position:absolute;left:0;top:682px;width:100%;text-align:center;font-size:8.3px;font-weight:700;color:#777}
.site-footer{position:absolute;left:6px;top:716px;width:800px;height:60px;background:var(--footer);color:#f2f2f2;font-size:11px;text-align:center;line-height:60px;letter-spacing:.3px}
</style>
</head>
<body>
<div class="site-logo"><span class="mark"></span><span class="name">klemvit</span></div>

<nav class="main-nav">
  <svg width="816" height="32" viewBox="0 0 816 32" aria-hidden="true">
    <polygon points="0,0 816,0 800,16 816,32 0,32 16,16" fill="#ffffff"/>
    <line x1="0" y1="32" x2="816" y2="32" stroke="#d9d0bc" stroke-width="1"/>
  </svg>
  <ul>
    <li style="left:101px">Home</li>
    <li style="left:251px">Products</li>
    <li class="active" style="left:402px">prices</li>
    <li style="left:546px">About</li>
    <li style="left:702px">Contact Us</li>
  </ul>
</nav>

<div class="hero-banner" role="img" aria-label="Photo of bamboo print blocks laid out on a grey surface"></div>

<main class="content-panel">
  <p class="body-copy intro">Bamboo is one of the fastest-growing plants on Earth, with reported growth rates of 250 cm (98 in) in 24 hours.[2] However, the growth rate is dependent on local soil and climatic conditions, as well as species, and a more typical growth rate for many commonly cultivated bamboos in temperate climates is in the range of 3–10 centimetres (1.2–3.9 in) per day during the growing period. Primarily growing in regions of warmer climates during the late Cretaceous period, vast fields existed in what is now Asia. Some of the largest timber bamboo can grow over 30 m (98 ft) tall, and be as large as 15–20 cm (5.9–7.9 in) in diameter. However, the size range for mature bamboo is species dependent, with the smallest bamboos reaching only several inches high at maturity. A typical height range that would cover many of the common bamboos grown in the United States is 4.6–12 metres (15–39 ft), depending on species. Anji County of China, known as the "Town of Bamboo", provides the optimal climate and soil conditions to grow, harvest, and process some of the most valued bamboo poles available worldwide.</p>

  <div class="promo-video" role="img" aria-label="Video still showing a photo being mounted on a bamboo panel"></div>

  <form class="upload-box">
    <div class="row">Filename: <span class="btn">Browse...</span> No file selected.</div>
    <div><span class="btn submit">Submit</span></div>
  </form>

  <p class="body-copy more">Most bamboo species flower infrequently. In fact, many bamboos only flower at intervals as long as 65 or 120 years. These taxa exhibit mass flowering (or gregarious flowering), with all plants in a particular species flowering worldwide over a several-year period. The longest mass flowering interval known is 130 years, and it is for the species Phyllostachys bambusoides (Sieb. &amp; Zucc.). In this species, all plants of the same stock flower at the same time, regardless of differences in geographic locations or climatic conditions, and then the bamboo dies. The lack of environmental impact on the time of flowering indicates the presence of some sort of “alarm clock” in each cell of the plant which signals the diversion of all energy to flower production and the cessation of vegetative growth.[12] This mechanism, as well as the evolutionary cause behind it, is still largely a mystery.</p>

  <div class="gallery">
    <div class="photo p1" role="img" aria-label="Hands placing a standing bamboo print block"></div>
    <div class="photo p2" role="img" aria-label="Rows of bamboo print blocks"></div>
    <div class="photo p3" role="img" aria-label="Trimming the edge of a bamboo print block"></div>
  </div>
  <p class="gallery-caption">The 2 options we have 2.5cm bamboo and 4cm bamboo hanging and standing</p>

  <footer class="site-footer">©2014 klemvit.com. All Rights Reserved.</footer>
</main>
</body>
</html>
```